Realtor resource

This is a website that provides resources for Realtors and their customers (home buyers and sellers).

There are 5 pages that I need redesigned:

1. Homepage: https://brightporchhelp.com/
2. Support Page/Contact Us: https://brightporchhelp.com/contact-us/
3. Agent Dashboard - See attached screenshot
4. Real Estate Documents page - See attached screenshot
5. Real Estate Contract page - see attached screenshot

Target Market(s)

Real estate agents and their customers.

Industry/Entity Type

Real Estate

Number of Pages Required

5+ page

Requirements
Must have
• Please use a modern design and incorporate design with current logo.

```html
<!DOCTYPE html>
<html lang="en">
<head>
<meta charset="utf-8">
<title>BrightPorchHelp – Real Estate Contracts</title>
<link href="https://fonts.googleapis.com/css2?family=Open+Sans:wght@400;600;700;800&display=swap" rel="stylesheet">
<style>
  :root {
    --ink: #111111;
    --paper: #ffffff;
    --accent: #f7941d;
    --rule: #222222;
    --photo-light: #eef0f2;
    --photo-mid: #c9d3dc;
    --photo-blue: #5d9bd5;
  }
  * { box-sizing: border-box; margin: 0; padding: 0; }
  html, body { width: 1200px; height: 675px; overflow: hidden; background: var(--paper); }
  body { font-family: "Open Sans", Arial, sans-serif; color: var(--ink); position: relative; }

  .site-header {
    position: absolute; left: 0; top: 0; width: 1088px; height: 53px;
    border-bottom: 1px solid var(--rule);
  }
  .brand {
    position: absolute; left: 112px; top: 13px;
    display: flex; align-items: center; gap: 6px;
    text-decoration: none; color: var(--ink);
    font-size: 21px; font-weight: 600; letter-spacing: -0.3px;
  }
  .brand-dot { width: 22px; height: 22px; border-radius: 50%; background: var(--accent); }
  .header-nav {
    position: absolute; right: 0; top: 20px;
    display: flex; gap: 21px; font-size: 10px; font-weight: 400;
  }
  .header-nav a { color: var(--ink); text-decoration: none; display: flex; align-items: center; gap: 6px; }
  .header-nav svg { width: 11px; height: 11px; fill: var(--ink); }

  .hero-copy {
    position: absolute; left: 130px; top: 260px; width: 440px; text-align: center;
  }
  .hero-title { font-size: 32px; font-weight: 800; letter-spacing: 0.3px; line-height: 1.1; }
  .hero-subtitle { font-size: 15.5px; font-weight: 400; margin-top: 5px; }

  .audience-links {
    position: absolute; left: 238px; top: 343px; display: flex; gap: 13px;
  }
  .audience-link {
    width: 105px; height: 105px; border-radius: 50%; background: var(--accent);
    color: var(--paper); text-decoration: none; text-align: center;
    display: flex; flex-direction: column; align-items: center; justify-content: flex-start;
    padding-top: 25px;
    font-size: 11.5px; font-weight: 700; line-height: 1.05;
  }
  .audience-link svg { width: 40px; height: 40px; margin-bottom: 6px; }
  .audience-link.agents svg { width: 36px; height: 36px; margin-bottom: 9px; }

  .hero-visual {
    position: absolute; left: 615px; top: 167px; width: 473px; height: 364px;
    background: linear-gradient(180deg, var(--photo-light) 0%, var(--photo-mid) 55%, var(--photo-blue) 100%);
    border-radius: 4px;
  }

  .site-footer {
    position: absolute; left: 112px; top: 638px; width: 1088px;
    border-top: 1px solid var(--rule);
  }
  .footer-meta {
    position: absolute; right: 112px; top: 10px; font-size: 10px; white-space: nowrap;
  }
  .footer-meta a { color: var(--ink); text-decoration: none; }
  .footer-meta .sep { margin: 0 9px; }
</style>
</head>
<body>
  <header class="site-header">
    <a class="brand" href="https://brightporchhelp.com/">BrightPorchHelp<span class="brand-dot"></span></a>
    <nav class="header-nav">
      <a href="https://brightporchhelp.com/contact-us/">
        <svg viewBox="0 0 12 12"><path d="M0 0h12v8H4l-3 3V8H0z"/></svg>SUPPORT
      </a>
      <a href="#login">
        <svg viewBox="0 0 12 12"><circle cx="6" cy="3.2" r="3"/><path d="M0 12c0-3.5 2.5-5 6-5s6 1.5 6 5z"/></svg>LOGIN
      </a>
    </nav>
  </header>

  <main>
    <section class="hero-copy">
      <h1 class="hero-title">REAL ESTATE CONTRACTS</h1>
      <p class="hero-subtitle">Explained in plain language by Texas real estate attorneys</p>
    </section>

    <nav class="audience-links">
      <a class="audience-link agents" href="#agents">
        <svg viewBox="0 0 36 36"><rect x="0" y="0" width="36" height="36" fill="#ffffff"/></svg>
        AGENTS
      </a>
      <a class="audience-link buyers-sellers" href="#buyers-sellers">
        <svg viewBox="0 0 40 40"><path d="M20 2 L39 19 H34 V38 H6 V19 H1 Z" fill="#ffffff"/><circle cx="20" cy="20" r="5" fill="#f7941d"/><rect x="18.5" y="23" width="3" height="10" fill="#f7941d"/><rect x="21" y="28" width="3" height="2" fill="#f7941d"/></svg>
        BUYERS &amp;<br>SELLERS
      </a>
    </nav>

    <div class="hero-visual" role="img" aria-label="Photo of a tall stack of contract papers with a small blue model house and a fountain pen in front"></div>
  </main>

  <footer class="site-footer">
    <p class="footer-meta"><a href="#terms">Terms &amp; Conditions</a><span class="sep">|</span>©2019 BrightPorchHelp.</p>
  </footer>
</body>
</html>
```